Boutique investment company is looking for money

We, Cardelith, are a very small boutique consulting and investment management firm in SWITZERLAND. Cardelith is trying to raise EUR 5-15 million in areas not easily accessible to private investors.

It will not be possible to raise these funds from traditional institutional investors because:
- Time and budget constraints
- Lack of track record in this particular area
Therefore, the capital has to be raised from in a non-conventional way, guerilla-style, from probably 10-15 private investors providing 1 million each. What can we offer? First, the money will be in Switzerland. Second, it will not be with a large bank – so, discretion is guaranteed. We are no-bullshit but data-driven, out of the box investors. We are different.

The site is only the bait to contact us. Maybe it should look like a presentation, just with additional elements for navigation. Maybe there should be one image or a chart explaining each page.

The site will be small, five pages, in two or three languages each.

Investors in Russia and South America

Boutique

Coded - Design and coding required

4 page

• Read the "Nice to Haves" section

Requirements
Must have
• If you have local insight to Russia and Southern America - use it.
• I am German and I love modern architecture - and I would like to see simple and logical design, including easy navigation.
• I am enclosing some files you may find useful. The graphics need to be consistent and can either be clean like they are now or look improvised and hand-drawn - if you can turn them consistently into that.
• We need a home page that should simply state "Safe, secure, Swiss" and then four pages: About Cardelith, Investment opportunity, Absolute return investing,
• Investment strategy. And the navigation needs to allow to toggle between English, Russian and Spanish.
• Let me help you by providing some examples of the kind of site that I have in mind, crisp, clean, simple (the sites are listed in alphabetical order):
• vemoridge.example
• tulsenfield.example
• quorvanholt.example
• zepharlind.example
• dormivelleco.example
• ketraholm.example
• lurovaspring.example
• pelmorath.example
• wistegrove.example
• fendralwick.example
• orbesquay.example
• jyn-halcrest.example
• Take a look at these and your job will become easier, much easier. They all have the same type of look and feel to them.
• One really cool landing page is here:
• wdlt.example
• Maybe we can do something like on their landing page in our logo with ursae minoris (see pictures)?
• If you use pictures, think Switzerland. Google the following and look at images:
• Matterhorn
• luzern vierwaldstättersee
• mechanical swiss watch
• vault
Nice to have
• Please look at the logo. I like the Sans Serif Fonts, Gill Sans and Helvetica Neue above all. Colors based on the logo are:
• - dark blue R: 0, G: 22, B: 115
• - light blue R: 68, G: 133, B: 212
Should not have
• Unless you feel that the audience loves pompous design, let's keep it straight.

```html
<!DOCTYPE html>
<html lang="en">
<head>
<meta charset="utf-8">
<title>Cardelith — Safe, Secure, Swiss</title>
<link href="https://fonts.googleapis.com/css2?family=Open+Sans:wght@400;600;700;800&display=swap" rel="stylesheet">
<style>
:root{
  --navy:#001673;
  --night:#050b2a;
  --deep:#0a1650;
  --sky:#4485d4;
  --royal:#1d4fae;
  --green:#3cbf8c;
  --red:#e2332b;
  --leaf:#4cae3a;
  --ink:#333;
  --muted:#666;
  --card:#3a3d44;
  --white:#fff;
}
*{box-sizing:border-box;margin:0;padding:0}
html,body{width:673px;height:1200px;overflow:hidden}
body{font-family:"Open Sans",Arial,sans-serif;color:var(--ink);background:var(--white);position:relative}

.site-header{position:absolute;top:0;left:0;width:673px;height:28px;background:var(--white);z-index:3}
.brand{position:absolute;left:14px;top:0;width:112px;height:62px;background:var(--white);
  clip-path:polygon(0 0,100% 0,100% 80%,50% 100%,0 80%);display:flex;flex-direction:column;align-items:center;justify-content:center;z-index:4}
.brand-name{font-weight:700;font-size:17px;color:var(--navy);display:flex;align-items:center;gap:5px}
.brand-name::before{content:"";width:8px;height:8px;border-radius:50%;background:var(--sky)}
.brand-tag{font-size:6px;color:var(--sky);margin-top:1px}
.main-nav{position:absolute;right:14px;top:11px;display:flex;gap:14px;font-size:6px;font-weight:600;color:var(--muted);text-transform:uppercase}
.main-nav .active{color:var(--navy)}
.lang{position:absolute;right:14px;top:0;background:var(--royal);color:var(--white);font-size:6px;padding:1px 7px;border-radius:0 0 2px 2px;z-index:5}

.hero{position:absolute;top:0;left:0;width:673px;height:300px;
  background:radial-gradient(ellipse at 60% 40%,#15204f 0%,var(--night) 70%)}

.claim{position:absolute;top:300px;left:0;width:673px;height:82px;background:var(--green);text-align:center;color:var(--white)}
.claim p{font-size:15px;font-weight:600;line-height:19px;padding-top:10px}
.btn-outline{display:inline-block;margin-top:6px;border:1.5px solid var(--white);border-radius:3px;padding:3px 20px;font-size:12px;font-weight:600}

.offer{position:absolute;top:382px;left:0;width:673px;height:290px;
  background:linear-gradient(180deg,#0d2f8f 0%,#1f56b8 55%,#123c8e 100%)}
.offer-title{margin:18px auto 0;width:673px;height:26px;background:rgba(255,255,255,.92);display:flex;align-items:center;justify-content:center;gap:10px;
  font-size:15px;font-weight:800;color:var(--navy)}
.offer-title::before,.offer-title::after{content:"";width:70px;height:2px;background:var(--navy)}
.cards{position:absolute;top:66px;left:139px;display:flex;gap:11px}
.card{width:124px;height:200px;background:var(--card);padding:7px;color:#ddd;text-align:center;box-shadow:0 3px 8px rgba(0,0,0,.4)}
.card-media{height:58px;background:linear-gradient(135deg,#d9dde3,#8e949c)}
.card h3{font-size:6.5px;font-weight:700;color:var(--white);margin:7px 0 5px;text-align:left}
.card p{font-size:5.5px;line-height:8px;text-align:left}
.btn-small{display:inline-block;margin-top:8px;background:var(--royal);color:var(--white);font-size:5.5px;font-weight:700;padding:3px 12px}

.swiss{position:absolute;top:672px;left:0;width:673px;height:223px}
.swiss h2{position:absolute;left:40px;top:28px;font-size:19px;font-weight:800;letter-spacing:.5px}
.swiss h2 .safe{color:var(--red)} .swiss h2 .secure{color:var(--leaf)} .swiss h2 .sw{color:var(--royal)}
.swiss p{position:absolute;left:40px;top:60px;width:270px;font-size:6.5px;line-height:10px;color:var(--muted)}
.btn-solid{position:absolute;left:40px;top:158px;background:var(--royal);color:var(--white);font-size:13px;font-weight:600;padding:5px 18px;border-radius:3px}
.chart{position:absolute;left:330px;top:20px}

.what{position:absolute;top:895px;left:0;width:673px;height:262px;background:var(--deep);color:var(--white)}
.what h2{position:absolute;left:40px;top:16px;font-size:18px;font-weight:700}
.what .intro{position:absolute;left:40px;top:46px;width:595px;font-size:5.5px;line-height:8.5px;color:#c8cfe6}
.tiles{position:absolute;left:40px;top:92px;display:flex;gap:11px}
.tile{width:140px}
.tile-media{height:96px}
.tile p{font-size:6px;font-weight:600;margin-top:5px;line-height:8px}
.m1{background:linear-gradient(135deg,#b9c6d6,#7e8b68)}
.m2{background:linear-gradient(135deg,#8fa8c8,#3b5b8c)}
.m3{background:linear-gradient(135deg,#d6b46a,#9a6f2e)}
.m4{background:linear-gradient(135deg,#c9b07a,#7d7565)}
.img-2{background:linear-gradient(135deg,#cfd4d9,#6f7a86)}
.img-3{background:linear-gradient(135deg,#dfe3e8,#9aa3ad)}

.site-footer{position:absolute;top:1157px;left:0;width:673px;height:43px;background:#070d33;color:#aab}
.foot-nav{position:absolute;left:40px;top:12px;display:flex;gap:12px;font-size:5.5px;font-weight:600;text-transform:uppercase}
.copy{position:absolute;left:40px;top:24px;font-size:5px}
.follow{position:absolute;right:40px;top:9px;font-size:6px;text-align:left}
.dots{display:flex;gap:4px;margin-top:4px}
.dots span{width:8px;height:8px;border-radius:50%;background:var(--sky)}
</style>
</head>
<body>
<header class="site-header">
  <div class="brand"><span class="brand-name">Cardelith</span><span class="brand-tag">swiss boutique</span></div>
  <nav class="main-nav">
    <span class="active">Home</span><span>About us</span><span>Investment opportunity</span><span>Absolute return investing</span><span>Contact</span>
  </nav>
  <span class="lang">English ▾</span>
</header>

<section class="hero" role="img" aria-label="Night sky star chart of the Ursa Minor constellation with labelled stars such as Polaris and Kochab"></section>

<section class="claim">
  <p>The work we have completed<br>allow us the position ourselves as experts in business</p>
  <span class="btn-outline">JOIN US!</span>
</section>

<section class="offer">
  <h2 class="offer-title">WHAT CAN WE OFFER</h2>
  <div class="cards">
    <article class="card">
      <div class="card-media" role="img" aria-label="Photo of a mechanical Swiss watch movement"></div>
      <h3>CAPITAL HELD IN SWITZERLAND</h3>
      <p>Your funds stay in Switzerland under strict local rules. We keep the structure lean, the reporting clear and every step of the process fully transparent to you.</p>
      <span class="btn-small">READ MORE</span>
    </article>
    <article class="card">
      <div class="card-media img-2" role="img" aria-label="Photo of a bank vault door"></div>
      <h3>DISCRETION IS GUARANTEED</h3>
      <p>We are not a large bank. A small circle of private investors, direct contact with the partners and quiet handling of every mandate from the very first day.</p>
      <span class="btn-small">READ MORE</span>
    </article>
    <article class="card">
      <div class="card-media img-3" role="img" aria-label="Photo of hands working on a laptop"></div>
      <h3>DATA DRIVEN DECISIONS</h3>
      <p>No noise, only numbers. Our models test each idea before capital moves, so we invest in areas private investors rarely reach with care and conviction.</p>
      <span class="btn-small">READ MORE</span>
    </article>
  </div>
</section>

<section class="swiss">
  <h2><span class="safe">SAFE,</span> <span class="secure">SECURE,</span> <span class="sw">SWISS</span></h2>
  <p>We are a small consulting and investment firm based in Switzerland, and we offer private investors the opportunity to access markets that are usually closed to them. Our approach combines systematic trading with careful risk control. We rely on data, not opinions, and every position is tested before it is taken. Capital is raised from a handful of private partners who value discretion, independence and a clear view of how their money is working for them. Returns are measured against managed futures benchmarks and reported openly each quarter.</p>
  <span class="btn-solid">READ MORE</span>
  <svg class="chart" width="310" height="190" viewBox="0 0 310 190" role="img" aria-label="Line chart comparing managed futures and trading system returns">
    <g font-size="6" fill="#666" font-family="Open Sans, sans-serif">
      <g stroke="#ddd" stroke-width=".6">
        <line x1="30" y1="10" x2="300" y2="10"/><line x1="30" y1="30" x2="300" y2="30"/>
        <line x1="30" y1="50" x2="300" y2="50"/><line x1="30" y1="70" x2="300" y2="70"/>
        <line x1="30" y1="90" x2="300" y2="90"/><line x1="30" y1="110" x2="300" y2="110"/>
        <line x1="30" y1="130" x2="300" y2="130"/>
      </g>
      <text x="8" y="12">120%</text><text x="8" y="32">100%</text><text x="12" y="52">80%</text>
      <text x="12" y="72">60%</text><text x="12" y="92">40%</text><text x="12" y="112">20%</text><text x="16" y="132">0%</text>
      <g transform="rotate(-50)">
      </g>
      <text x="32" y="150" transform="rotate(-45 32 150)">Jan 07</text>
      <text x="62" y="150" transform="rotate(-45 62 150)">Jan 08</text>
      <text x="92" y="150" transform="rotate(-45 92 150)">Jan 09</text>
      <text x="122" y="150" transform="rotate(-45 122 150)">Jan 10</text>
      <text x="152" y="150" transform="rotate(-45 152 150)">Jan 11</text>
      <text x="182" y="150" transform="rotate(-45 182 150)">Jan 12</text>
      <text x="212" y="150" transform="rotate(-45 212 150)">Jan 13</text>
      <text x="242" y="150" transform="rotate(-45 242 150)">Jan 14</text>
      <text x="272" y="150" transform="rotate(-45 272 150)">Jan 15</text>
      <polyline fill="none" stroke="#9fb0d8" stroke-width="1.2" points="30,128 60,118 90,112 120,114 150,104 180,100 210,96 240,92 270,88 300,80"/>
      <polyline fill="none" stroke="#2a4fae" stroke-width="1.4" points="30,129 60,122 90,110 120,104 150,94 180,84 210,70 240,62 270,44 300,22"/>
      <line x1="90" y1="180" x2="102" y2="180" stroke="#9fb0d8" stroke-width="1.5"/><text x="105" y="182">Managed Futures</text>
      <line x1="175" y1="180" x2="187" y2="180" stroke="#2a4fae" stroke-width="1.5"/><text x="190" y="182">Trading System</text>
    </g>
  </svg>
</section>

<section class="what">
  <h2>What We Do</h2>
  <p class="intro">We help a small group of private investors place capital in areas that traditional institutions rarely serve. Every mandate starts with a clear conversation about goals, time horizon and risk. We then build a focused portfolio, test it against real market data and report back in plain language. Our partners in Russia and South America value the calm of Switzerland and the independence of a boutique that answers only to them.</p>
  <div class="tiles">
    <div class="tile"><div class="tile-media m1" role="img" aria-label="Photo of a modern city skyline"></div><p>Private placements in growing urban markets</p></div>
    <div class="tile"><div class="tile-media m2" role="img" aria-label="Photo of a Swiss lake and mountains"></div><p>Long term wealth kept safe in Switzerland</p></div>
    <div class="tile"><div class="tile-media m3" role="img" aria-label="Photo of stacked gold bars"></div><p>Real assets that protect against inflation</p></div>
    <div class="tile"><div class="tile-media m4" role="img" aria-label="Photo of banknotes and coins"></div><p>Absolute return strategies for any market</p></div>
  </div>
</section>

<footer class="site-footer">
  <nav class="foot-nav"><span>Home</span><span>About us</span><span>Investment opportunity</span><span>Absolute return investing</span><span>Contact</span></nav>
  <p class="copy">© Cardelith. All rights reserved.</p>
  <div class="follow">Follow us<div class="dots"><span></span><span></span><span></span><span></span></div></div>
</footer>
</body>
</html>
```